Flyer Design Project

We are a restaurant meal delivery service. We deliver from a variety of restaurants. We would like a flyer that will promote our service to busy commuters. The flyer will be distributed at local train stations. I would like the flyer to say something like "What's for dinner?" or "Meet us at your place!" or anything that is catchy.
In the flyer we want the customer to order online at our website plumcartmeals.com and use coupon code $5off. Using the coupon code will get them $5 off of their online purchase.
We would like to pass the flyers out in the morning and have the customers go online either on the train or at work to schedule the food to be delivered for dinner.
Target Market(s)
Hungry commuters that are in a rush 30 - 50 women
Industry/Entity Type
Restaurant

```html
<!DOCTYPE html>
<html lang="en">
<head>
<meta charset="utf-8">
<title>Plumcart Meals – Flyer</title>
<link href="https://fonts.googleapis.com/css2?family=Bebas+Neue&family=Open+Sans:wght@400;600&display=swap" rel="stylesheet">
<style>
  :root{
    --red:#e0141b;
    --red-dark:#b40d12;
    --charcoal:#2f3133;
    --paper:#eceeee;
    --card:#f6f7f7;
    --ink:#2b2b2b;
    --white:#ffffff;
  }
  *{margin:0;padding:0;box-sizing:border-box}
  html,body{width:933px;height:1200px;overflow:hidden;background:var(--paper)}
  .flyer{position:relative;width:933px;height:1200px;background:var(--paper);font-family:"Open Sans",Arial,sans-serif;color:var(--ink)}
  .display{font-family:"Bebas Neue",Impact,sans-serif;letter-spacing:.5px}

  .hero{position:absolute;left:0;top:0;width:933px;height:560px;
    background:radial-gradient(ellipse at 45% 55%,#e9c56a 0%,#d98a3a 28%,#b8452a 48%,#6d7a3a 72%,#3c4a2a 100%)}

  .coupon{position:absolute;left:0;top:29px;width:378px;height:88px;background:var(--red);
    clip-path:polygon(0 0,94% 0,100% 50%,94% 100%,0 100%);color:var(--white);padding:8px 0 0 31px}
  .coupon__code{font-size:33px;line-height:1}
  .coupon__note{font-size:15px;line-height:20px;margin-top:2px}

  .brand-ribbon{position:absolute;left:576px;top:0;width:310px;height:306px;background:var(--red);
    clip-path:polygon(0 0,100% 0,100% 100%,0 86%);display:flex;align-items:center;justify-content:center;flex-direction:column;gap:12px}
  .brand-ribbon__mark{width:34px;height:34px;border-radius:50%;background:var(--white)}
  .brand-ribbon__name{font-family:"Bebas Neue",Impact,sans-serif;color:var(--white);font-size:54px;line-height:1}

  .tagline-band{position:absolute;left:140px;top:527px;width:674px;height:66px;background:var(--charcoal);
    clip-path:polygon(6% 0,94% 0,100% 50%,94% 100%,6% 100%,0 50%)}
  .tagline{position:absolute;left:197px;top:530px;width:560px;height:60px;background:var(--red);
    clip-path:polygon(3% 0,97% 0,100% 50%,97% 100%,3% 100%,0 50%);color:var(--white);
    font-size:44px;display:flex;align-items:center;justify-content:center;padding-top:4px}

  .steps{position:absolute;left:21px;top:612px;width:893px}
  .step{position:absolute;top:0;width:292px}
  .step:nth-child(1){left:0}
  .step:nth-child(2){left:298px}
  .step:nth-child(3){left:597px}
  .step__photo{position:absolute;left:5px;top:0;width:282px;height:233px;border-radius:12px}
  .step__photo--pizza{background:linear-gradient(135deg,#e8c79a,#c2432a 55%,#f1ede6)}
  .step__photo--wings{background:linear-gradient(135deg,#8a2a1a,#c2321e 50%,#e6e4dc)}
  .step__photo--steak{background:linear-gradient(135deg,#c9803a,#5a2b1a 55%,#f0ece6)}
  .step__badge{position:absolute;left:175px;top:148px;width:104px;height:104px;background:var(--red);
    clip-path:polygon(100% 50%,90.6% 60.9%,93.3% 75%,79.7% 79.7%,75% 93.3%,60.9% 90.6%,50% 100%,39.1% 90.6%,25% 93.3%,20.3% 79.7%,6.7% 75%,9.4% 60.9%,0 50%,9.4% 39.1%,6.7% 25%,20.3% 20.3%,25% 6.7%,39.1% 9.4%,50% 0,60.9% 9.4%,75% 6.7%,79.7% 20.3%,93.3% 25%,90.6% 39.1%);
    color:var(--white);font-size:58px;display:flex;align-items:center;justify-content:center;padding-top:6px}
  .step__label{position:absolute;left:0;top:257px;width:292px;height:88px;background:var(--card);text-align:center;padding-top:10px}
  .step__title{font-size:33px;line-height:1;color:var(--ink)}
  .step__text{font-size:20px;line-height:26px}

  .order-band{position:absolute;left:0;top:977px;width:933px;height:67px;background:var(--charcoal)}
  .order{position:absolute;left:197px;top:979px;width:560px;height:63px;background:var(--red);
    clip-path:polygon(3% 0,97% 0,100% 50%,97% 100%,3% 100%,0 50%);color:var(--white);
    font-size:43px;display:flex;align-items:center;justify-content:center;padding-top:4px}

  .contact{position:absolute;left:21px;top:1063px;width:442px;height:103px;background:var(--card);padding:18px 0 0 37px}
  .contact__row{display:flex;align-items:center;gap:18px;height:24px;font-size:17px;color:var(--charcoal)}
  .contact__row svg{width:22px;height:18px;fill:none;stroke:var(--charcoal);stroke-width:2}
  .address{position:absolute;left:482px;top:1063px;width:430px;height:103px;background:var(--card);
    text-align:right;padding:18px 34px 0 0;font-size:19px;line-height:24px;color:var(--charcoal)}
  .address__name{color:var(--red)}
</style>
</head>
<body>
<main class="flyer">
  <div class="hero" role="img" aria-label="Photo of glazed salmon fillet on herbed rice with peppers and broccoli"></div>

  <div class="coupon">
    <div class="coupon__code display">Coupon code: $5OFF</div>
    <p class="coupon__note">Use coupon code to get $5 off of your online purchase</p>
  </div>

  <div class="brand-ribbon">
    <span class="brand-ribbon__mark"></span>
    <span class="brand-ribbon__name">Plumcart Meals</span>
  </div>

  <div class="tagline-band"></div>
  <h1 class="tagline display">Meet us at your place!</h1>

  <section class="steps">
    <div class="step">
      <div class="step__photo step__photo--pizza" role="img" aria-label="Photo of pepperoni and mushroom pizza"></div>
      <div class="step__badge display">1</div>
      <div class="step__label"><h2 class="step__title display">Search</h2><p class="step__text">Choose your restaurant</p></div>
    </div>
    <div class="step">
      <div class="step__photo step__photo--wings" role="img" aria-label="Photo of buffalo wings with dip and celery"></div>
      <div class="step__badge display">2</div>
      <div class="step__label"><h2 class="step__title display">Order</h2><p class="step__text">Choose your meal</p></div>
    </div>
    <div class="step">
      <div class="step__photo step__photo--steak" role="img" aria-label="Photo of grilled steak with asparagus"></div>
      <div class="step__badge display">3</div>
      <div class="step__label"><h2 class="step__title display">Relax</h2><p class="step__text">Your meal is on its way</p></div>
    </div>
  </section>

  <div class="order-band"></div>
  <div class="order display">Order online: plumcartmeals.com</div>

  <section class="contact display">
    <div class="contact__row">
      <svg viewBox="0 0 22 18"><path d="M2 6c3-4 15-4 18 0l-3 2-2-2H7L5 8z"/><path d="M5 9h12v7H5z"/></svg>
      <span>(555) 014-3000 | (555) 014-5439</span>
    </div>
    <div class="contact__row">
      <svg viewBox="0 0 22 18"><rect x="2" y="3" width="18" height="12"/><path d="M2 3l9 7 9-7"/></svg>
      <span>contact@plumcartmeals.com</span>
    </div>
    <div class="contact__row">
      <svg viewBox="0 0 22 18"><path d="M9 11l4-4"/><path d="M7 9l-3 3a2.5 2.5 0 0 0 4 4l3-3"/><path d="M15 9l3-3a2.5 2.5 0 0 0-4-4l-3 3"/></svg>
      <span>www.plumcartmeals.com</span>
    </div>
  </section>

  <address class="address display" style="font-style:normal">
    <div class="address__name">Plumcart Meals</div>
    <div>2200 Linden Ave, Suite B</div>
    <div>Maple Grove, IL 60410</div>
  </address>
</main>
</body>
</html>
```